Harborline Optical -Window Poster (Optometrist)

We are an optometry practice and we need a poster for a new store promotion for our window highlighting we now also sell 2 pairs of glasses as a package deal. The size will be 1300mm width x 1900mm height

The artwork will be displayed as a fabric banner in our shop window. We have 7 other banners with different services our business provides. The words needs to standout for passers by and the cars stopped at the traffic lights out front of our business. We already have signs with our logos phone number etc. so we won't need them included in the poster.

It would need to include the following information.

Two pair packages now available*

*Conditions apply
Updates

The artwork will be displayed as a fabric banner in our shop window. We have 7 other banners with different services our business provides. The words needs to standout for passers by and the cars stopped at the traffic lights out front of our business. We already have signs with our logos phone number etc. so we won't need them included in the poster. Thank you for your work it's amazing Added Saturday, February 18, 2017

The artwork will be displayed as a fabric banner in our shop window. We have 7 other banners with different services our business provides. The words needs to standout for passers by and the cars stopped at the traffic lights out front of our business. We already have signs with our logos phone number etc. so we won't need them included in the poster. Added Saturday, February 18, 2017

Target Market(s)

Cars driving past and stopped at traffic lights outside our store.

Industry/Entity Type

Optician

Requirements
Must have
• Poster must say:
• Two pair packages now available*
• *Conditions apply

```html
<!DOCTYPE html>
<html lang="en">
<head>
<meta charset="utf-8">
<title>Harborline Optical – Two Pair Packages Window Poster</title>
<link href="https://fonts.googleapis.com/css2?family=Philosopher:wght@700&display=swap" rel="stylesheet">
<style>
  :root {
    --paper: #eeeeee;
    --paper-light: #f3f3f3;
    --paper-shade: #e9e9e9;
    --fold: #dcdcdc;
    --headline-blue: #2a7db8;
    --note-grey: #7f8c8d;
  }
  html, body {
    margin: 0;
    padding: 0;
    overflow: hidden;
    background: var(--paper);
  }
  .poster {
    position: relative;
    width: 821px;
    height: 1200px;
    overflow: hidden;
  }
  .poster-art {
    display: block;
    width: 821px;
    height: 1200px;
  }
  .headline {
    font-family: "Philosopher", "Trebuchet MS", sans-serif;
    font-weight: 700;
    fill: var(--headline-blue);
  }
  .conditions {
    font-family: "Philosopher", "Trebuchet MS", sans-serif;
    font-weight: 700;
    fill: var(--note-grey);
  }
</style>
</head>
<body>
  <main class="poster">
    <svg class="poster-art" viewBox="0 0 821 1200" xmlns="http://www.w3.org/2000/svg">
      <defs>
        <linearGradient id="panel-top-left" x1="0" y1="0" x2="1" y2="1">
          <stop offset="0" stop-color="#efefef"/>
          <stop offset="1" stop-color="#f6f6f6"/>
        </linearGradient>
        <linearGradient id="panel-top-right" x1="1" y1="0" x2="0" y2="1">
          <stop offset="0" stop-color="#eeeeee"/>
          <stop offset="1" stop-color="#ebebeb"/>
        </linearGradient>
        <linearGradient id="panel-bottom-left" x1="0" y1="0" x2="1" y2="1">
          <stop offset="0" stop-color="#ebebeb"/>
          <stop offset="1" stop-color="#eeeeee"/>
        </linearGradient>
        <linearGradient id="panel-bottom-right" x1="0" y1="0" x2="1" y2="1">
          <stop offset="0" stop-color="#ececec"/>
          <stop offset="1" stop-color="#efefef"/>
        </linearGradient>
      </defs>

      <g class="paper-panels">
        <rect x="0" y="0" width="409" height="600" fill="url(#panel-top-left)"/>
        <rect x="409" y="0" width="412" height="600" fill="url(#panel-top-right)"/>
        <rect x="0" y="600" width="409" height="600" fill="url(#panel-bottom-left)"/>
        <rect x="409" y="600" width="412" height="600" fill="url(#panel-bottom-right)"/>
        <line class="fold-line" x1="409" y1="0" x2="409" y2="1200" stroke="var(--fold)" stroke-width="1"/>
        <line class="fold-line" x1="0" y1="600" x2="821" y2="600" stroke="var(--fold)" stroke-width="1"/>
      </g>

      <g class="headline-block">
        <text class="headline" x="412" y="376" font-size="128" text-anchor="middle"
              textLength="688" lengthAdjust="spacingAndGlyphs">TWO PAIR</text>
        <text class="headline" x="415" y="587" font-size="96" text-anchor="middle"
              textLength="812" lengthAdjust="spacingAndGlyphs">PACKAGES NOW</text>
        <text class="headline" x="402" y="820" font-size="130" text-anchor="middle"
              textLength="793" lengthAdjust="spacingAndGlyphs">AVAILABLE*</text>
      </g>

      <text class="conditions" x="400" y="1108" font-size="52" text-anchor="middle"
            textLength="478" lengthAdjust="spacingAndGlyphs">*Conditions apply</text>
    </svg>
  </main>
</body>
</html>
```